Thank you for shopping with us business card

We would like a thank you card for our rebranded business. We used to be "Kestrel Knacks" but are now "Kestrel Trinkets. Old thank you card and new logo will be attached for reference. New thank you card does not have to be same design as old thank you card, but please use new logo.
Mopsa URL is now kestreltrinkets.mopsa.com
Pictaloo is @Kestrel_Trinkets
Email is kestreltrinkets@mopsamail.com
Thank you!

Contact Information for Business Card

Mopsa site, email, Pictaloo

```html
<!DOCTYPE html>
<html lang="en">
<head>
<meta charset="utf-8">
<title>Kestrel Trinkets – Thank You Card</title>
<link href="https://fonts.googleapis.com/css2?family=Outfit:wght@400;500&family=Mr+Dafoe&family=Libre+Baskerville:wght@700&display=swap" rel="stylesheet">
<style>
  :root {
    --navy: #0f2747;
    --navy-pattern: #0d2343;
    --white: #ffffff;
    --cyan: #3fb8e6;
    --star: #f7ea1c;
    --page: #ffffff;
  }
  * { box-sizing: border-box; margin: 0; padding: 0; }
  html, body {
    width: 1200px; height: 1100px; overflow: hidden;
    background: var(--page);
    font-family: "Outfit", sans-serif;
    color: var(--white);
  }
  .canvas { position: relative; width: 1200px; height: 1100px; }

  .card {
    position: absolute; left: 225px; width: 750px; height: 429px;
    background: var(--navy);
  }
  .card--front { top: 95px; }
  .card--back { top: 576px; }

  /* front */
  .front-pattern { position: absolute; inset: 0; background: var(--navy-pattern); }
  .front-mark {
    position: absolute; left: 315px; top: 100px; width: 120px; height: 120px;
    border: 6px solid var(--white); border-radius: 50%;
  }
  .front-name {
    position: absolute; left: 0; right: 0; top: 315px;
    text-align: center; font-size: 29px; font-weight: 500; letter-spacing: 0.3px;
  }

  /* back header */
  .back-header {
    position: absolute; left: 0; top: 0; width: 100%; height: 157px;
    border-bottom: 2px solid var(--white);
  }
  .thanks-script {
    position: absolute; left: 0; right: 0; top: 0;
    text-align: center; font-family: "Mr Dafoe", cursive;
    font-size: 92px; line-height: 1; color: var(--white); z-index: 2;
  }
  .thanks-line {
    position: absolute; left: 0; right: 0; top: 76px;
    text-align: center; font-family: "Libre Baskerville", serif; font-weight: 700;
    font-size: 41px; color: var(--cyan); letter-spacing: -0.5px;
  }

  /* back body */
  .divider {
    position: absolute; left: 341px; top: 214px; width: 2px; height: 215px;
    background: var(--white);
  }
  .brand {
    position: absolute; left: 28px; top: 214px; display: flex; align-items: center;
  }
  .brand-square { width: 44px; height: 44px; background: var(--white); }
  .brand-rule { width: 1px; height: 60px; background: var(--white); margin: 0 16px 0 20px; }
  .brand-name { font-size: 19px; font-weight: 500; line-height: 1.3; letter-spacing: 0.3px; }

  .contacts { position: absolute; left: 26px; top: 309px; list-style: none; }
  .contacts li {
    display: flex; align-items: center; height: 34px;
    font-size: 16.5px; letter-spacing: 0.2px;
  }
  .contact-icon { width: 24px; height: 24px; margin-right: 12px; flex: none; }

  .message { position: absolute; left: 375px; top: 208px; width: 340px; }
  .message-lead { font-size: 21px; line-height: 29px; letter-spacing: 0.2px; }
  .message-review { margin-top: 16px; font-size: 18.5px; line-height: 25px; }
  .stars { display: flex; gap: 10px; margin-top: 10px; }
  .star { width: 26px; height: 26px; fill: var(--star); }
</style>
</head>
<body>
<main class="canvas">

  <section class="card card--front" aria-label="Card front">
    <div class="front-pattern" role="img" aria-label="Subtle tonal repeating brand pattern"></div>
    <div class="front-mark"></div>
    <p class="front-name">KESTREL TRINKETS</p>
  </section>

  <section class="card card--back" aria-label="Card back">
    <header class="back-header">
      <p class="thanks-script">Thank You</p>
      <p class="thanks-line">for your Purchase</p>
    </header>

    <div class="brand">
      <div class="brand-square"></div>
      <div class="brand-rule"></div>
      <p class="brand-name">KESTREL<br>TRINKETS</p>
    </div>

    <ul class="contacts">
      <li>
        <svg class="contact-icon" viewBox="0 0 24 24"><circle cx="12" cy="12" r="11" fill="#fff"/></svg>
        kestreltrinkets.mopsa.com
      </li>
      <li>
        <svg class="contact-icon" viewBox="0 0 24 24"><rect x="2" y="2" width="20" height="20" rx="3" fill="#fff"/></svg>
        @Kestrel_Trinkets
      </li>
      <li>
        <svg class="contact-icon" viewBox="0 0 24 24"><rect x="1" y="5" width="22" height="15" fill="#fff"/><path d="M1 5 L12 14 L23 5" fill="none" stroke="#0f2747" stroke-width="2"/></svg>
        kestreltrinkets@mopsamail.com
      </li>
    </ul>

    <div class="divider"></div>

    <div class="message">
      <p class="message-lead">Your purchase made my day and I hope this package brightens yours.</p>
      <p class="message-review">Please come back and leave a review!</p>
      <div class="stars" aria-label="Five stars">
        <svg class="star" viewBox="0 0 24 24"><path d="M12 1l3.3 7.1 7.7.8-5.8 5.2 1.7 7.6L12 17.8 5.1 21.7l1.7-7.6L1 8.9l7.7-.8z"/></svg>
        <svg class="star" viewBox="0 0 24 24"><path d="M12 1l3.3 7.1 7.7.8-5.8 5.2 1.7 7.6L12 17.8 5.1 21.7l1.7-7.6L1 8.9l7.7-.8z"/></svg>
        <svg class="star" viewBox="0 0 24 24"><path d="M12 1l3.3 7.1 7.7.8-5.8 5.2 1.7 7.6L12 17.8 5.1 21.7l1.7-7.6L1 8.9l7.7-.8z"/></svg>
        <svg class="star" viewBox="0 0 24 24"><path d="M12 1l3.3 7.1 7.7.8-5.8 5.2 1.7 7.6L12 17.8 5.1 21.7l1.7-7.6L1 8.9l7.7-.8z"/></svg>
        <svg class="star" viewBox="0 0 24 24"><path d="M12 1l3.3 7.1 7.7.8-5.8 5.2 1.7 7.6L12 17.8 5.1 21.7l1.7-7.6L1 8.9l7.7-.8z"/></svg>
      </div>
    </div>
  </section>

</main>
</body>
</html>
```